Nutrigenomics Business card design

Nutrigenomics is an exciting emerging field where I sequence the DNA from a saliva swab and then tailor a personalised nutritional program according to the persons genetics. It is possible to turn down undesirable genes that may be stuck "on" all the time causing inflammation etc. Equally important we switch "on" genes that might be stuck "off" as is often the case with autism. A large portion of my clients are autistic children. We see huge changes in functionality with the appropriate changes in diet to regulate their gene expression. This technology is definitely the way of the future.
I need a logo that will clearly show the combination of genetics with nutrition. The word "Nutrigenomics" still isn't in common use yet. I'm thinking maybe a DNA helix - (I think most people associate a helix with DNA or genes, but I'm open to suggestions) Combined somehow with food - preferably vegetables/ fruit/ meat/eggs etc. Definitely not grains or dairy - we take autistic kids off those 2 food groups straight away.
Green in it somewhere? I somehow associates healthy living / whole foods nutrition with the colour green. You guys know more about colours than me :-)
Maybe a helix could morph into a body shape filled with foods (along the lines of "you are what you eat" or something...)

Target Market(s)

The majority of my clients to date are people in their 40's wanting to improve their health or their children's health.

Industry/Entity Type

Nutrition

Contact Information for Business Card

Front of card:
Dr Moira Pellton (B App Sci, PhD Molecular Pathology)
Certified Vitacorde Practitioner and RUNE Nutritionist
52 Tallowby Rd, Tallowby
0417386254
dr.moirapellton@quillmail.com
drmoirapellton.com.au
Back of card:
Small Photo of me, Dr Moira Pellton
Specialises in Autism, ADHD, Fussy Eaters, Gut Issues, Food Intolerances, Healthy Ageing

Logo Text

Dr Moira Pellton

Logo styles of interest
Pictorial/Combination Logo
Character Logo
Requirements
Must have
• A logo showing a clear link between genes and nutrition
The box for what I want written on the card is not coming up when I try to edit so I'll put it here....
Front of card:
Dr Moira Pellton
(B App Sci, PhD Molecular Pathology) in smaller writing under my name

Certified Nutrigenomist
Certified RUNE Nutritionist

then use your nice symbols for the address, ph etc as below

52 Tallowby Rd, Tallowby
0417386254
dr.moirapellton@quillmail.com
www.drmoirapellton.com.au

Back of card:
Small Photo of me
Dr Moira Pellton
Specialises in:
Nutrigenomics
Healthy Ageing
Autism / ADHD
Gut Issues
Food Intolerances
Should not have
• No bread or grains of any sort
No dairy - milk cheese etc

```html
<!DOCTYPE html>
<html lang="en">
<head>
<meta charset="utf-8">
<title>Dr Moira Pellton – Business Card</title>
<link href="https://fonts.googleapis.com/css2?family=Tenor+Sans&family=Alegreya+Sans:wght@400&display=swap" rel="stylesheet">
<style>
  :root{
    --bg:#000000;
    --card-white:#ffffff;
    --forest:#0a6235;
    --leaf:#4c9a2a;
    --ink:#1a1a1a;
    --on-green:#ffffff;
    --rule:#9cc2a9;
    --photo-a:#6b4a3a;
    --photo-b:#c89a80;
  }
  *{margin:0;padding:0;box-sizing:border-box}
  html,body{width:1200px;height:849px;overflow:hidden;background:var(--bg)}
  .canvas{position:relative;width:1200px;height:849px}
  .card{position:absolute;top:322px;width:358px;height:204px;border-radius:10px;overflow:hidden}
  .card--front{left:228px;background:var(--card-white);color:var(--ink)}
  .card--back{left:613px;background:var(--forest);color:var(--on-green)}

  .contact{position:absolute;left:171px;top:13px;list-style:none;font-family:"Tenor Sans",sans-serif;font-size:9.6px;line-height:11.4px}
  .contact li{display:flex;align-items:center;gap:7px}
  .contact li:last-child{margin-top:2px}
  .contact svg{width:8px;height:8px;flex:none}

  .name{position:absolute;left:15px;top:140px;font-family:"Tenor Sans",sans-serif;font-size:16px;font-weight:400;color:var(--forest);white-space:nowrap}
  .quals{position:absolute;left:14px;top:169px;font-family:"Tenor Sans",sans-serif;font-size:7.6px;white-space:nowrap}
  .brand-mark{position:absolute;left:171px;top:98px;width:46px;height:46px;background:var(--leaf)}
  .certs{position:absolute;left:222px;top:152px;font-family:"Tenor Sans",sans-serif;font-size:9.6px;line-height:11px;white-space:nowrap}

  .portrait{position:absolute;left:149px;top:17px;width:61px;height:81px;border-radius:3px;background:linear-gradient(180deg,var(--photo-a),var(--photo-b))}
  .back-name{position:absolute;left:0;right:0;top:105px;text-align:center;font-family:"Tenor Sans",sans-serif;font-size:15px;font-weight:400}
  .divider{position:absolute;left:0;right:0;top:146px;height:1px;background:var(--rule)}
  .specialties{position:absolute;left:19px;top:156px;font-family:"Alegreya Sans",sans-serif;font-size:8.8px;line-height:14px;white-space:nowrap}
  .specialties ul{list-style:none;display:flex;gap:8px}
  .specialties li::before{content:"• "}
</style>
</head>
<body>
<div class="canvas">
  <section class="card card--front">
    <ul class="contact">
      <li><svg viewBox="0 0 8 8"><rect x="0.5" y="1.5" width="7" height="5" fill="#1a1a1a"/><path d="M0.5 1.5 4 4.5 7.5 1.5" stroke="#fff" stroke-width="0.8" fill="none"/></svg>52 Tallowby Rd, Tallowby</li>
      <li><svg viewBox="0 0 8 8"><path d="M1.5 0.8 3 0.8 3.6 2.6 2.6 3.4Q3.4 5 4.8 5.6L5.6 4.6 7.3 5.2 7.3 6.7Q4 7.2 1.4 4 0.6 2.2 1.5 0.8Z" fill="#1a1a1a"/></svg>0417386254</li>
      <li><svg viewBox="0 0 8 8"><rect x="0.5" y="1.5" width="7" height="5" rx="1" fill="#1a1a1a"/><circle cx="4" cy="4" r="1.4" fill="#fff"/></svg>dr.moirapellton@quillmail.com</li>
      <li><svg viewBox="0 0 8 8"><circle cx="4" cy="4" r="3.3" fill="none" stroke="#1a1a1a" stroke-width="0.9"/><path d="M0.7 4H7.3M4 0.7Q2 4 4 7.3M4 0.7Q6 4 4 7.3" stroke="#1a1a1a" stroke-width="0.7" fill="none"/></svg>www.drmoirapellton.com.au</li>
    </ul>
    <div class="brand-mark" aria-hidden="true"></div>
    <h1 class="name">Dr Moira Pellton</h1>
    <p class="quals">(B App Sci, PhD Molecular Pathology)</p>
    <p class="certs">Certified Nutrigenomist<br>Certified RUNE Nutritionist</p>
  </section>

  <section class="card card--back">
    <div class="portrait" role="img" aria-label="Small portrait photo of Dr Moira Pellton"></div>
    <h2 class="back-name">Dr Moira Pellton</h2>
    <div class="divider"></div>
    <div class="specialties">
      <p>Specialises in:</p>
      <ul>
        <li>Nutrigenomics</li>
        <li>Healthy Ageing</li>
        <li>Autism / ADHD</li>
        <li>Gut Issues</li>
        <li>Food Intolerances</li>
      </ul>
    </div>
  </section>
</div>
</body>
</html>
```